International Detailing Product Manufacturer Needs Wash & Wax Auto Soap Packaging Design

We are launching an Automotive Soap (Wash & Wax) to add to our line of Detail products under the brand name Copper Falcon Detail Products. Our customers are all over the country and find our products at Big Box Retailers such as Tru-Mart Stores, Car Depot, McKinnon, Tam Crew etc.

Take a look at Shinework Labs Ultra Coat Wash & Wax with Tone Reviving Formula (64 oz - 1/2 Gal). This is exactly the type of packaging we will be using. In terms of dimensions, the label will be going on a 1/2 Gallon Broad side rectangular jug just like the Shinework Labs product mentioned.

Target Market(s)

25-65 Male, This product is for car enthusiasts and car care professionals. Young enthusiasts who are new to protecting their automotive investments as well as seasons auto-enthusiasts who may have a weekend car they enjoy maintaining

Industry/Entity Type

Automotive

Font styles to use
Serif

Requirements
Must have
• This label must call out a special feature of our Auto Wash formula. Our Wash features Salt & Brine resistant detergents. This means the detergents (the ingredient in the soap that is responsible for suds/cleaning power) do not break down when in contact with Salt and/or Brine.

Normally soap in a bucket, or soap sprayed onto a vehicle directly begins to lose its power as salt/brine breaks the detergents down, rendering the soap useless. Our formula allows for ultra suds that don't break down, no matter how many times your rag is dipped in the wash bucket. Our formula disperses thicker suds that do not dissipate as they work to dislodge contaminants from the paint.
Nice to have
• There are so many gimmicky looking options on the market for this type of product. Customers are conditioned to see flashy packaging. We want to sport attractive colors, and portray an extremely fun experience WHILE ALSO delivering a absolutely premium image. This soap is going to be high priced compared to competitors because it truly is better performing. We would like this label to portray a seriousness, and a professional grade image. I want this label to look like the top shelf stuff!
Should not have
• Nothing to add to this section at this time

```html
<!DOCTYPE html>
<html lang="en">
<head>
<meta charset="utf-8">
<title>Copper Falcon Wash &amp; Wax Label</title>
<link rel="stylesheet" href="https://fonts.googleapis.com/css2?family=Rubik:wght@700;900&family=Arimo:wght@700&family=Oswald:wght@400&display=swap">
<style>
  :root {
    --page: #f2f2f2;
    --label: #000000;
    --ink: #ffffff;
    --ink-shadow: #2b2b2b;
    --brand: #e2562c;
    --sphere-light: #3ed2f0;
    --sphere-mid: #2a6fd6;
    --sphere-deep: #3a2f8f;
  }
  html, body {
    margin: 0;
    width: 1200px;
    height: 1200px;
    overflow: hidden;
    background: var(--page);
  }
  .canvas {
    position: relative;
    width: 1200px;
    height: 1200px;
  }
  .label {
    position: absolute;
    left: 100px;
    top: 137px;
    width: 1000px;
    height: 927px;
    background: var(--label);
    border-radius: 18px;
    overflow: hidden;
    color: var(--ink);
    text-align: center;
  }
  .brand {
    position: absolute;
    left: 0;
    right: 0;
    top: 60px;
    font-family: "Rubik", sans-serif;
    font-weight: 700;
    color: var(--brand);
    line-height: 1.05;
  }
  .brand-name { font-size: 62px; }
  .brand-sub { font-size: 26px; letter-spacing: 4px; text-transform: uppercase; margin-top: 8px; }
  .bubbles {
    position: absolute;
    left: 0;
    top: 0;
    width: 1000px;
    height: 927px;
  }
  .kicker {
    position: absolute;
    left: 0; right: 0;
    top: 360px;
    font-family: "Arimo", sans-serif;
    font-weight: 700;
    font-size: 40px;
    letter-spacing: -0.5px;
    text-shadow: 2px 2px 0 var(--ink-shadow);
  }
  .product-name {
    position: absolute;
    left: 0; right: 0;
    top: 415px;
    font-family: "Rubik", sans-serif;
    font-weight: 900;
    font-size: 136px;
    line-height: 1;
    letter-spacing: -1px;
    text-shadow: 5px 5px 0 var(--ink-shadow);
  }
  .feature {
    position: absolute;
    left: 0; right: 0;
    top: 560px;
    font-family: "Rubik", sans-serif;
    font-weight: 700;
    font-size: 62px;
    line-height: 1.15;
    text-shadow: 3px 3px 0 var(--ink-shadow);
  }
  .volume {
    position: absolute;
    left: 0; right: 0;
    top: 828px;
    font-family: "Oswald", sans-serif;
    font-weight: 400;
    font-size: 46px;
    line-height: 1;
  }
</style>
</head>
<body>
<div class="canvas">
  <section class="label">
    <svg class="bubbles" viewBox="0 0 1000 927" role="img" aria-label="Illustration of glossy blue and purple soap bubbles with small sparkles">
      <defs>
        <radialGradient id="sphere-fill" cx="0.35" cy="0.3" r="0.75">
          <stop offset="0" stop-color="var(--sphere-light)"/>
          <stop offset="0.55" stop-color="var(--sphere-mid)"/>
          <stop offset="1" stop-color="var(--sphere-deep)"/>
        </radialGradient>
      </defs>
      <circle cx="517" cy="512" r="262" fill="url(#sphere-fill)"/>
    </svg>
    <div class="brand">
      <div class="brand-name">Copper Falcon</div>
      <div class="brand-sub">Detail Products</div>
    </div>
    <div class="kicker">AUTOMOTIVE SOAP</div>
    <h1 class="product-name" style="margin:0">Wash &amp; Wax</h1>
    <div class="feature">Salt &amp; Brine<br>Resistant</div>
    <div class="volume">64 oz - 1/2 Gal</div>
  </section>
</div>
</body>
</html>
```